rk ironcraft business card metallic look

revamp the existing design but want card to have a metalic look to it

Target Market(s)

construction industry

Industry/Entity Type

constrction

Contact Information for Business Card

front of card RK Ironcraft, phone 4165550193, email rk.ironcraftt@veltrano.com and instagram account; rk_ironcraft_

Font styles to use
Other font styles liked:
• masculine

Colors

Designer to choose only greyscale colors for use in the design.

Requirements
Must have
• back side RK Ironcraft then a list of everything : Siding, ACM Panels, Standing Seam,Soffit, Fascia, Gutters,Metal,Alu,inum, Viynyl, Metal Roofs and roof repairs
Nice to have
• I would like to keep the look of the existing card with the metal grids on the front
Should not have
• Need a design in two days

```html
<!DOCTYPE html>
<html lang="en">
<head>
<meta charset="utf-8">
<title>RK Ironcraft – Business Card</title>
<link rel="stylesheet" href="https://fonts.googleapis.com/css2?family=Orbitron:wght@600;800&family=Roboto:wght@700&display=swap">
<style>
  :root {
    --page: #ffffff;
    --card-black: #0e0e0e;
    --card-charcoal: #2a2a2a;
    --panel-dark: #181818;
    --steel-light: #e4e4e4;
    --steel-mid: #b9b9b9;
    --steel-edge: #d8d8d8;
    --corner-grey: #474747;
    --ink: #0a0a0a;
    --chrome: #c9c9c9;
    --contact: #d0d0d0;
  }
  html, body {
    margin: 0;
    width: 1200px;
    height: 1200px;
    overflow: hidden;
    background: var(--page);
  }
  .sheet { position: relative; width: 1200px; height: 1200px; }
  .card { position: absolute; left: 229px; width: 750px; height: 428px; display: block; }
  .card--front { top: 149px; }
  .card--back { top: 631px; }
  .brand-initials { font-family: "Orbitron", sans-serif; font-weight: 800; fill: var(--chrome); }
  .brand-word { font-family: "Orbitron", sans-serif; font-weight: 800; fill: var(--chrome); }
  .contact-text { font-family: "Roboto", sans-serif; font-weight: 700; font-size: 15px; fill: var(--contact); }
  .contact-icon { fill: var(--contact); }
  .service-line { font-family: "Orbitron", sans-serif; font-weight: 600; font-size: 33px; fill: var(--ink); }
</style>
</head>
<body>
<main class="sheet">

  <!-- Front of card -->
  <svg class="card card--front" viewBox="0 0 750 428" xmlns="http://www.w3.org/2000/svg">
    <defs>
      <radialGradient id="brushed-dark" cx="45%" cy="50%" r="70%">
        <stop offset="0" stop-color="#3a3a3a"/>
        <stop offset="0.6" stop-color="#1c1c1c"/>
        <stop offset="1" stop-color="#0a0a0a"/>
      </radialGradient>
      <linearGradient id="rib-panel" x1="0" y1="0" x2="1" y2="0">
        <stop offset="0" stop-color="#2a2a2a"/>
        <stop offset="0.5" stop-color="#4a4a4a"/>
        <stop offset="1" stop-color="#2e2e2e"/>
      </linearGradient>
    </defs>
    <rect class="front-base" width="750" height="428" fill="url(#brushed-dark)"/>
    <polygon class="corner-plate" points="0,0 200,0 0,116" fill="var(--corner-grey)"/>
    <line x1="0" y1="116" x2="200" y2="0" stroke="#8a8a8a" stroke-width="1.5"/>
    <polygon class="ribbed-panel" role="img" aria-label="Corrugated metal panel texture"
             points="475,37 510,0 750,0 750,165 725,177" fill="url(#rib-panel)"/>
    <polygon class="edge-shard" points="595,257 750,170 750,428 545,428 750,300 750,295" fill="var(--card-black)"/>
    <polygon points="545,415 750,295 750,428 520,428" fill="var(--card-black)"/>
    <line x1="595" y1="257" x2="733" y2="171" stroke="#e0e0e0" stroke-width="3"/>
    <line x1="545" y1="415" x2="750" y2="295" stroke="#e0e0e0" stroke-width="3"/>

    <text class="brand-initials" x="371" y="200" text-anchor="middle" font-size="86">RK</text>
    <text class="brand-word" x="371" y="237" text-anchor="middle" font-size="25" textLength="328" lengthAdjust="spacingAndGlyphs">IRONCRAFT</text>

    <g class="contact contact--phone">
      <circle class="contact-icon" cx="257" cy="274" r="8"/>
      <path d="M253.5 270.5 l2 -1 l1.5 2.5 l-1.2 1 q1 2 3 3 l1 -1.2 l2.5 1.5 l-1 2 q-5 0 -7.8 -7.8z" fill="var(--card-black)"/>
      <text class="contact-text" x="277" y="279">416-555-0193</text>
    </g>
    <g class="contact contact--email">
      <rect x="246" y="296" width="22" height="14" fill="none" stroke="var(--contact)" stroke-width="1.5"/>
      <path d="M246 296 l11 8 l11 -8 M246 310 l8 -7 M268 310 l-8 -7" fill="none" stroke="var(--contact)" stroke-width="1.5"/>
      <text class="contact-text" x="282" y="307">rk.ironcraftt@veltrano.com</text>
    </g>
    <g class="contact contact--social">
      <rect class="contact-icon" x="248" y="323" width="17" height="17" rx="2"/>
      <text class="contact-text" x="280" y="336">rk_ironcraft_</text>
    </g>
  </svg>

  <!-- Back of card -->
  <svg class="card card--back" viewBox="0 0 750 428" xmlns="http://www.w3.org/2000/svg">
    <defs>
      <linearGradient id="brushed-steel" x1="0" y1="0" x2="1" y2="1">
        <stop offset="0" stop-color="#b4b4b4"/>
        <stop offset="0.35" stop-color="#e6e6e6"/>
        <stop offset="0.7" stop-color="#c4c4c4"/>
        <stop offset="1" stop-color="#dedede"/>
      </linearGradient>
    </defs>
    <rect class="back-base" width="750" height="428" fill="url(#brushed-steel)"/>
    <polygon class="edge-bevel" points="0,0 74,0 432,376 405,428 0,428" fill="#5a5a5a"/>
    <polygon class="dark-panel" points="0,0 67,0 425,376 398,428 0,428" fill="var(--panel-dark)"/>

    <text class="brand-initials" x="146" y="308" text-anchor="middle" font-size="64">RK</text>
    <text class="brand-word" x="146" y="334" text-anchor="middle" font-size="19" textLength="218" lengthAdjust="spacingAndGlyphs">IRONCRAFT</text>

    <g class="service-list">
      <text class="service-line" x="192" y="85" textLength="444" lengthAdjust="spacingAndGlyphs">Siding, ACM Panels,</text>
      <text class="service-line" x="234" y="127" textLength="498" lengthAdjust="spacingAndGlyphs">Standing Seam, Soffit,</text>
      <text class="service-line" x="269" y="170" textLength="353" lengthAdjust="spacingAndGlyphs">Fascia, Gutters,</text>
      <text class="service-line" x="307" y="210" textLength="410" lengthAdjust="spacingAndGlyphs">Metal, Alumunium,</text>
      <text class="service-line" x="332" y="251" textLength="146" lengthAdjust="spacingAndGlyphs">Viynyl,</text>
      <text class="service-line" x="387" y="292" textLength="271" lengthAdjust="spacingAndGlyphs">Metal Roofs</text>
      <text class="service-line" x="421" y="326" textLength="200" lengthAdjust="spacingAndGlyphs">and roof</text>
      <text class="service-line" x="454" y="357" textLength="165" lengthAdjust="spacingAndGlyphs">repairs</text>
    </g>
  </svg>

</main>
</body>
</html>
```